| 希望する色 | 特になし・その他 追記事項: ブランドカラーについて添付URLに記載あり |
【 依頼内容 】 介護×美容を両方学べる社会人向けプロスクール「ひだまり整容学舎」のSNS広告バナーデザインを募集します。 当校HP:https://tsubakiho.jp/ ・配信媒体:Facebook / Instagram広告(フィード・ストーリーズ)/LINE広告 ・画像サイズ:1080px × 1080px(ピクセル) ※採用した方は追加で、1080px × 1920pxサイズの作成も依頼する場合がございます。 ・基本フォントは「游ゴシック」でお願いします ※手書き風のメッセージなど、明朝体のほうがバランスが良いなど理由がある場合は可。 遷移先のLP・作成用の素材・過去の制作物については添付URLをご参照ください。 【 契約金額(税抜) 】 5000円/デザイン (追加でサイズ違いの依頼の場合は2000円/デザイン) 3~5デザイン採用予定です! ※契約金額(税込)からシステム利用料を差し引いた金額が、ワーカーさまの受取金額となります 【依頼の目的】 SNS広告のキャッチコピーでターゲットの興味をグッと惹きつけ、Webページに誘導してまずは当スクールの資料請求をしてもらうことです。 (※SNS広告のイメージは添付ファイルをご覧ください) ターゲットは主に2種類いらっしゃいます 優先度髙【昔美容師をしていたが、出産でブランクがある。ママさん美容師】 ・子育ても落ち着いてきたので、美容師に戻ろうと思っている(戻った)が、拘束時間が長くなかな昔みたいに働けない。家庭との両立が難しいと考えている。 ⇒訪問美容師は遅くても夕方までの勤務なので、今までの経験を活かして働くことが出来ることを知らないママさん美容師に向けた、家庭との両立と副業感覚で短時間で稼げる事に興味を持ってもらう。 優先度低【美容師としてサロンに勤めている30歳前後】 ・独立も視野にあるスタイリスト経験ある美容師。一般的な美容院を作って独立することを視野にあるが、開業資金も高く美容室が増えているので不安がある。 ⇒お店を構えなくても良い「訪問美容師」なら、すぐに独立でき、高齢者が増えているのでこの先安泰では?と思えるようなコピー。 【依頼の背景】 ・訪問美容師とは? 主に介護施設や外出が困難な方向けに、こちらから訪問してカット・カラーなどの美容施術を行います。 ・訪問美容師の昔と今の違い 昔から、どの施設にもボランティアや理美容師さんが訪問をしてカットをしているが、昨今美容が好きな高齢者が増えている背景もあり、ただ髪を短くするだけじゃなく、美容室に行ったときのような施術を求められます。 ※ボランティアではなかなか実現しにくくなっている また、現在の訪問美容師さんは介護の知識を持っており、高齢者の応対もできるので、施設やご家族からは安心してもらえるのが、最近のスタンダードになっています。 ・訪問美容師のお仕事状況(弊社から依頼している案件ベース) 平日夕方までの実働:基本的には介護施設でご利用者さんの活動時間に訪問をする為 値段:地域性はあるが、カットお一人3000円~4500円ほどと一般的なサロンと変わらない値段 魅力:施設に伺う場合、お客様を選ぶというよりは毎週決まった時間に訪問して、施術を行うので、タイムスケジュールが決めやすいので、サロン勤務や家庭との両立も可能 ・ひだまり整容学舎で何を学ぶの? 訪問美容師デビューに向けた、テクニック、ビジネス、介護の初任者研修(資格取得)の講座を受けれる社会人向けスクール ※こちら参考にしてください※ 東京のビジネス講座の講師は、当校の1期生です。 参考Facebookページ:https://www.nakamaweb-sns.jp/tsubakiho.jp/posts/530287164912358 【重視するポイント】 ・「もっと知りたい!」「やってみたい!」とターゲットの興味を喚起し、クリックしてもらうことが目的です。 ・SNS広告で使用するので、表示された時に1秒で伝わるわかりやすさとインパクトは必須だと考えています。 ・文字数に具体的な制限はありませんが、トンマナも含め添付ファイルの既存広告をご参照ください。 【重要事項】 ①当校の広告は、スクールであることを重視しております。 業界的にも、画像的にも、よくご高齢者様に対してのサービスだと思われがちです。 そのサービスを提供する人材育成のスクールであることを念頭に入れて頂けると幸いです。 ②よりクリックしたく思わせるような「ティザー」の要素を加えて頂きたいです。 ※よく使うティザー例(違うフレーズでもOKです) 「今、訪問美容師が求められている3つの理由」 「家庭との両立が取りやすい理由とは?」 「ひだまり整容学舎が選ばれる理由とは?」 【年末年始について】 12/25~1/4まで冬期休暇をいただいております。 お問い合わせの回答にお時間を頂戴する場合がございますので、ご了承くださいませ。 その他ご質問等ありましたら、気軽にお問い合わせください。 ご応募をお待ちしております! |
| https://files.nerimo-docs.jp/document/d/8vQ2tRw5ZkLp0aXcYm3Hn7JsBd4FgEu9WiOy6TrKlMbN/edit | ||

```html
<!DOCTYPE html>
<html lang="ja">
<head>
<meta charset="utf-8">
<title>ひだまり整容学舎 — 訪問美容師という選択</title>
<link href="https://fonts.googleapis.com/css2?family=Noto+Sans+JP:wght@500;700;900&display=swap" rel="stylesheet">
<style>
  :root {
    --bg: #fbf1ec;
    --ink: #1f1f1f;
    --pink: #e4097f;
    --green: #12a04a;
    --yellow: #fff04a;
    --orange: #e8651c;
    --bubble: #ef2f86;
    --band: #ffffff;
    --photo-a: #c9a38c;
    --photo-b: #8f5a45;
    --stripe-1: #e4097f;
    --stripe-2: #f7c600;
    --stripe-3: #12a04a;
    --stripe-4: #3aa3dc;
    --stripe-5: #f08a1c;
  }
  * { margin: 0; padding: 0; box-sizing: border-box; }
  html, body { width: 1200px; height: 1200px; overflow: hidden; }
  body {
    font-family: "Noto Sans JP", sans-serif;
    color: var(--ink);
  }
  .banner {
    position: relative;
    width: 1200px;
    height: 1200px;
    background: var(--bg);
    overflow: hidden;
  }
  .top-stripe {
    position: absolute; top: 0; left: 0; width: 100%; height: 14px;
    display: flex;
  }
  .top-stripe span { flex: 1; }
  .top-stripe span:nth-child(1) { background: var(--stripe-1); }
  .top-stripe span:nth-child(2) { background: var(--stripe-2); }
  .top-stripe span:nth-child(3) { background: var(--stripe-3); }
  .top-stripe span:nth-child(4) { background: var(--stripe-4); }
  .top-stripe span:nth-child(5) { background: var(--stripe-5); }

  .headline {
    position: absolute; top: 62px; left: 0; width: 100%;
    text-align: center;
    font-weight: 900;
    font-size: 98px;
    line-height: 1.2;
    letter-spacing: 2px;
  }
  .headline .accent-pink { color: var(--pink); }
  .headline .accent-green { color: var(--green); }

  .lead {
    position: absolute; top: 310px; left: 0; width: 100%;
    text-align: center;
    font-weight: 900;
    font-size: 46px;
    line-height: 1.75;
  }
  .lead .highlight {
    color: var(--orange);
    background: var(--yellow);
    padding: 0 8px;
  }

  .photo {
    position: absolute; top: 0; left: 0;
  }

  .teaser {
    position: absolute; left: 710px; top: 615px;
    width: 400px; height: 150px;
    color: #fff; text-align: center;
  }
  .teaser svg { position: absolute; inset: 0; }
  .teaser p { position: relative; font-weight: 900; white-space: nowrap; }
  .teaser .teaser-main { font-size: 38px; padding-top: 22px; line-height: 1.3; }
  .teaser .teaser-sub { font-size: 28px; line-height: 1.45; }

  .footer-band {
    position: absolute; left: 0; bottom: 0; width: 100%; height: 175px;
    background: var(--band);
    display: flex; align-items: center;
    padding: 0 50px 0 60px;
  }
  .school-name {
    flex: none;
    display: flex; align-items: center; gap: 16px;
    font-weight: 700; font-size: 38px; color: var(--ink);
    white-space: nowrap;
  }
  .school-name .mark {
    width: 38px; height: 38px; background: var(--pink);
  }
  .tagline {
    margin-left: auto;
    font-weight: 900; font-size: 34px; color: var(--ink);
    white-space: nowrap;
  }
</style>
</head>
<body>
  <main class="banner">
    <div class="top-stripe"><span></span><span></span><span></span><span></span><span></span></div>

    <h1 class="headline">
      <span class="accent-pink">あなた</span>を待っている<br>
      <span class="accent-green">人</span>がいます。
    </h1>

    <p class="lead">
      ママになっても、キャリアを諦めない！<br>
      キレイを届ける<span class="highlight">「訪問美容師」</span>という選択。
    </p>

    <svg class="photo" width="1200" height="1030" viewBox="0 0 1200 1030" role="img" aria-label="訪問美容師がフェイスシールドを着けて利用者の髪をカットしている写真">
      <defs>
        <linearGradient id="photoTone" x1="0" y1="0" x2="1" y2="1">
          <stop offset="0" stop-color="var(--photo-a)"/>
          <stop offset="1" stop-color="var(--photo-b)"/>
        </linearGradient>
      </defs>
      <path d="M0 600 C 120 540, 260 580, 420 555 C 600 525, 760 560, 900 545 C 1060 528, 1160 580, 1190 670 C 1215 780, 1160 910, 1120 1030 L 0 1030 Z" fill="url(#photoTone)"/>
    </svg>

    <div class="teaser">
      <svg width="400" height="175" viewBox="0 0 400 175" aria-hidden="true">
        <rect x="0" y="0" width="400" height="150" rx="75" fill="var(--bubble)"/>
        <path d="M70 135 L40 175 L115 142 Z" fill="var(--bubble)"/>
      </svg>
      <p class="teaser-main">仕事と家庭。</p>
      <p class="teaser-sub">両立しやすい理由とは？</p>
    </div>

    <footer class="footer-band">
      <div class="school-name"><span class="mark"></span>ひだまり整容学舎</div>
      <p class="tagline">日本初！「介護×美容」の専門プロスクール</p>
    </footer>
  </main>
</body>
</html>
```